GDFH Business Card

Looking for a business card design to incorporate our branding. We want to only use the colors listing in the Branding Package (attached).
Updates

Target Market(s)

People who need their phone or device fixed.

Industry/Entity Type

Electronics

Contact Information for Business Card

Please use:

Gadget Fix Haven LLC
4870 S Ridgecrest Pkwy
Suite 318
San Antonio, TX 78291

Wendell Thorsby, Store Manager

(210) 555-0147

Requirements
Must have
• Must include the colors that are contained within the Branding Package PDF file.

```html
<!DOCTYPE html>
<html lang="en">
<head>
<meta charset="utf-8">
<title>Gadget Fix Haven Business Card</title>
<link rel="stylesheet" href="https://fonts.googleapis.com/css2?family=Roboto:wght@300;400&display=swap">
<style>
  :root {
    --backdrop: #2b2623;
    --card-black: #111111;
    --card-black-deep: #050505;
    --card-gray: #5c5c5c;
    --brand-orange: #f0531f;
    --text-light: #f2f2f2;
    --text-muted: #d6d6d6;
    --divider: #e6e6e6;
  }
  html, body {
    margin: 0;
    padding: 0;
    width: 1200px;
    height: 810px;
    overflow: hidden;
    background: var(--backdrop);
    font-family: "Roboto", Arial, sans-serif;
  }
  .canvas {
    position: relative;
    width: 1200px;
    height: 810px;
  }
  .card {
    position: absolute;
    width: 500px;
    height: 286px;
    border-radius: 16px;
    overflow: hidden;
    box-shadow: 0 14px 30px rgba(0,0,0,0.45);
  }
  .card-front {
    left: 70px;
    top: 110px;
    background: linear-gradient(160deg, #222 0%, var(--card-black) 60%, #0c0c0c 100%);
  }
  .card-back {
    left: 630px;
    top: 410px;
    background: var(--card-black-deep);
  }
  .card-shapes {
    position: absolute;
    inset: 0;
  }
  .brand {
    position: absolute;
    display: flex;
    align-items: center;
    gap: 12px;
  }
  .card-front .brand {
    left: 50%;
    top: 50%;
    transform: translate(-50%, -50%);
  }
  .card-back .brand {
    right: 40px;
    top: 30px;
  }
  .brand-square {
    width: 34px;
    height: 34px;
    border-radius: 7px;
    background: var(--brand-orange);
  }
  .brand-name {
    font-weight: 300;
    font-size: 27px;
    color: var(--brand-orange);
    letter-spacing: 0.3px;
    white-space: nowrap;
  }
  .person {
    position: absolute;
    left: 48px;
    top: 156px;
    color: var(--text-light);
  }
  .person-name {
    font-weight: 300;
    font-size: 23px;
    margin: 0;
  }
  .person-title {
    font-weight: 300;
    font-size: 12px;
    margin: 3px 0 0;
    color: var(--text-muted);
  }
  .divider {
    position: absolute;
    left: 222px;
    top: 162px;
    width: 1px;
    height: 90px;
    background: var(--divider);
  }
  .contact {
    position: absolute;
    left: 240px;
    top: 192px;
    margin: 0;
    padding: 0;
    list-style: none;
    color: var(--text-light);
    font-weight: 300;
    font-size: 15px;
  }
  .contact li {
    display: flex;
    align-items: center;
    gap: 10px;
    margin-bottom: 16px;
    white-space: nowrap;
  }
  .contact svg {
    width: 15px;
    height: 15px;
    flex: none;
  }
</style>
</head>
<body>
<main class="canvas">

  <section class="card card-front" aria-label="Card front">
    <div class="brand">
      <span class="brand-square"></span>
      <span class="brand-name">Gadget Fix Haven</span>
    </div>
  </section>

  <section class="card card-back" aria-label="Card back">
    <svg class="card-shapes" viewBox="0 0 500 286" preserveAspectRatio="none" aria-hidden="true">
      <polygon points="0,88 16,88 40,116 430,176 500,176 500,286 0,286" fill="var(--card-gray)"/>
      <polyline points="22,80 46,106 430,166 480,166" fill="none" stroke="var(--brand-orange)" stroke-width="5"/>
    </svg>

    <div class="brand">
      <span class="brand-square"></span>
      <span class="brand-name">Gadget Fix Haven</span>
    </div>

    <div class="person">
      <p class="person-name">Wendell Thorsby</p>
      <p class="person-title">Store Manager</p>
    </div>

    <div class="divider"></div>

    <ul class="contact">
      <li>
        <svg viewBox="0 0 16 16" aria-hidden="true"><rect width="16" height="16" rx="2" fill="var(--text-light)"/><path d="M5 3.5c-.8.5-1.2 1.4-.9 2.4.6 2.5 2.5 4.6 5 5.8.9.4 1.9.1 2.5-.6l-1.6-1.6-1.2.7c-1-.5-1.9-1.5-2.4-2.6l.8-1.1z" fill="var(--card-gray)"/></svg>
        <span>(210) 555-0147</span>
      </li>
      <li>
        <svg viewBox="0 0 16 16" aria-hidden="true"><rect width="16" height="16" rx="2" fill="var(--text-light)"/><rect x="3" y="5" width="10" height="7" fill="none" stroke="var(--card-gray)" stroke-width="1.2"/><path d="M3 5l5 4 5-4" fill="none" stroke="var(--card-gray)" stroke-width="1.2"/></svg>
        <span>wendell@GadgetFixHaven.com</span>
      </li>
    </ul>
  </section>

</main>
</body>
</html>
```